Company website design for Marlowfen Pricing Counsel LLC

Design of company website. See uploaded outline. Logo hex codes for the icon colors: middle blue - 4D6C8A, dark blue - 11122B.

```html
<!DOCTYPE html>
<html lang="en">
<head>
<meta charset="utf-8">
<title>Marlowfen Pricing Counsel LLC</title>
<link href="https://fonts.googleapis.com/css2?family=Lato:wght@400;700;900&display=swap" rel="stylesheet">
<style>
:root{
  --blue:#4d6c8a;
  --navy:#11122b;
  --ink:#1b1c2a;
  --mist:#e5ecec;
  --white:#ffffff;
  --text:#3a3d4a;
  --line:#c9d2d8;
}
*{margin:0;padding:0;box-sizing:border-box}
html,body{width:1200px;height:3699px;overflow:hidden}
body{position:relative;background:var(--white);font-family:'Lato',sans-serif;color:var(--text)}
.abs{position:absolute}

/* header */
.site-header{left:0;top:0;width:1200px;height:82px;background:var(--white)}
.brand{left:75px;top:20px;display:flex;align-items:center;gap:10px}
.brand-mark{width:42px;height:42px;background:var(--navy)}
.brand-name{font-weight:700;font-size:25px;letter-spacing:1px;color:var(--navy);line-height:1}
.brand-name small{display:block;font-size:11px;letter-spacing:2.6px;margin-top:4px;font-weight:400}
.nav{top:33px;font-size:14px;font-weight:700;color:var(--ink);display:flex;align-items:center;gap:6px}
.nav.active{color:var(--blue)}
.nav i{display:inline-block;width:11px;height:11px;background:var(--blue)}

/* hero */
.hero{left:0;top:82px;width:1200px;height:740px}
.hero-title{left:75px;top:290px;font-size:68px;font-weight:900;line-height:64px;color:var(--white)}
.hero-sub{left:75px;top:433px;font-size:34px;line-height:35px;color:var(--white)}
.btn{display:flex;align-items:center;justify-content:center;border-radius:20px;font-weight:700;color:var(--white);font-size:15px}
.hero-btn{left:75px;top:534px;width:155px;height:37px;background:var(--blue)}

/* values */
.values-title{left:0;top:843px;width:1200px;text-align:center;font-size:28px;font-weight:700;color:var(--ink)}
.values-list{left:0;top:898px;width:1200px;text-align:center;font-size:18px;font-weight:700;color:var(--blue);letter-spacing:.3px}
.values-list span{margin:0 11px;color:var(--blue)}

/* what we do */
.section-heading{font-size:43px;font-weight:900;color:var(--white)}
.section-copy{font-size:15.5px;line-height:25.5px;color:#e8ebef;width:320px}
.outline-btn{border:2px solid var(--white);background:transparent}
.service-card{background:var(--white);border-radius:6px;box-shadow:0 3px 14px rgba(17,18,43,.15);width:335px;height:199px}
.service-icon{position:absolute;left:18px;top:20px;width:62px;height:66px;border:2px solid #3b3e4c;border-radius:4px}
.service-title{position:absolute;left:103px;top:17px;font-size:20px;font-weight:700;line-height:24px;color:var(--blue);width:225px}
.service-text{position:absolute;left:103px;top:74px;font-size:13.5px;line-height:21px;color:var(--text);width:222px}

/* who we serve */
.serve-title{left:0;top:1732px;width:1200px;text-align:center;font-size:41px;font-weight:900;color:var(--ink)}
.tile{width:331px;height:254px;border-radius:5px;overflow:hidden;box-shadow:0 3px 10px rgba(17,18,43,.2)}
.tile-band{position:absolute;left:0;top:95px;width:100%;height:66px;background:rgba(30,32,40,.6);display:flex;align-items:center;justify-content:center;font-size:24px;font-weight:700;color:var(--white)}

/* contact */
.form-card{left:433px;top:2727px;width:694px;height:331px;background:var(--white);border-radius:6px;box-shadow:0 3px 14px rgba(17,18,43,.15)}
.field{border:1.5px solid var(--line);border-radius:20px;font-size:13px;color:#555;padding-left:22px;display:flex;align-items:center}
.msg{border:1.5px solid var(--line);border-radius:14px;font-size:13px;color:#555;padding:14px 42px}
.captcha{border:1px solid #d3d3d3;background:#f9f9f9;border-radius:3px;box-shadow:0 1px 3px rgba(0,0,0,.1)}

/* footer */
.foot-head{font-size:17px;font-weight:700;color:var(--ink)}
.foot-rule{height:1.5px;width:153px;background:#a8b3bc}
.foot-links{font-size:12.5px;line-height:28px;color:var(--ink)}
.foot-info{font-size:12.5px;line-height:22px;color:var(--ink)}
.foot-info b{color:var(--blue)}
.bottom-bar{left:0;top:3639px;width:1200px;height:60px;background:var(--navy)}
.copyright{left:75px;top:22px;font-size:12px;color:var(--white)}
.social{top:19px;width:22px;height:22px;border-radius:50%;background:var(--white)}
</style>
</head>
<body>

<!-- header -->
<header class="abs site-header">
  <div class="abs brand">
    <div class="brand-mark"></div>
    <div class="brand-name">MARLOWFEN<small>PRICING COUNSEL LLC</small></div>
  </div>
  <div class="abs nav active" style="left:524px"><i></i>Home</div>
  <div class="abs nav" style="left:620px"><i></i>Services</div>
  <div class="abs nav" style="left:736px"><i></i>Who Do We Serve</div>
  <div class="abs nav" style="left:897px"><i></i>Industries</div>
  <div class="abs nav" style="left:1026px"><i></i>Contact Us</div>
</header>

<!-- hero -->
<svg class="abs hero" viewBox="0 0 1200 740" width="1200" height="740">
  <defs>
    <linearGradient id="heroFill" x1="0" y1="0" x2="0" y2="1">
      <stop offset="0" stop-color="#7f8a94"/>
      <stop offset="0.35" stop-color="#8f7f74"/>
      <stop offset="0.55" stop-color="#9a5c3c"/>
      <stop offset="0.75" stop-color="#5a5448"/>
      <stop offset="1" stop-color="#a8813f"/>
    </linearGradient>
  </defs>
  <polygon role="img" aria-label="Mountain range at sunset above a grassy valley with a ranch fence" points="0,0 1200,0 1200,538 0,740" fill="url(#heroFill)"/>
  <polygon points="1200,538 623,643 1200,740" fill="#4d6c8a"/>
</svg>
<h1 class="abs hero-title">Building a Business<br>is a Journey</h1>
<p class="abs hero-sub">We have the valuation expertise<br>to guide you.</p>
<div class="abs btn hero-btn">Read More &nbsp;»</div>

<!-- values -->
<h2 class="abs values-title">Our Values</h2>
<p class="abs values-list">INTEGRITY<span>|</span>RESPONSIVENESS<span>|</span>EXCELLENCE<span>|</span>RELATIONSHIPS<span>|</span>COMMUNITY</p>

<!-- what we do -->
<svg class="abs" style="left:0;top:990px" width="620" height="490" viewBox="0 0 620 490">
  <defs>
    <linearGradient id="meetFill" x1="0" y1="0" x2="1" y2="1">
      <stop offset="0" stop-color="#3a3f48"/>
      <stop offset="1" stop-color="#16181e"/>
    </linearGradient>
  </defs>
  <polygon role="img" aria-label="Dark photo of colleagues meeting around a laptop" points="0,0 474,0 614,490 0,490" fill="url(#meetFill)"/>
</svg>
<h2 class="abs section-heading" style="left:75px;top:1092px">What We Do</h2>
<p class="abs section-copy" style="left:75px;top:1152px">Sed ut perspiciatis unde omnis iste natus error sit voluptatem accusantium doloremque laudantium, totam rem aperiam, eaque ipsa quae ab illo&nbsp; inventore veritatis et quasi architecto beatae vitae dicta sunt explicabo.</p>
<div class="abs btn outline-btn" style="left:77px;top:1331px;width:137px;height:36px">Read More »</div>

<div class="abs service-card" style="left:433px;top:1025px">
  <div class="service-icon" role="img" aria-label="Line icon of a tax document with calculator"></div>
  <div class="service-title">Tax-Related<br>Valuations</div>
  <div class="service-text">Valuations for estate/gift tax, charitable contributions, equity-linked&nbsp; compensation, corporate restructuring and insolvency purposes.</div>
</div>
<div class="abs service-card" style="left:792px;top:1025px">
  <div class="service-icon" role="img" aria-label="Line icon of two advisors in conversation"></div>
  <div class="service-title">Financing &amp;Transaction Advisory</div>
  <div class="service-text">Financial assessments to evaluate debt structure and capital adequacy. Valuation support for loan underwriting, capital raises, share redemptions.</div>
</div>
<div class="abs service-card" style="left:433px;top:1246px">
  <div class="service-icon" role="img" aria-label="Line icon of a report with charts"></div>
  <div class="service-title">Financial<br>Reporting</div>
  <div class="service-text">Our work includes purchase price allocations, fresh-start accounting, impairment analyses, equity-linked compensation, leases and financial instruments.</div>
</div>
<div class="abs service-card" style="left:792px;top:1246px">
  <div class="service-icon" role="img" aria-label="Line icon of a presenter at a planning board"></div>
  <div class="service-title">Business Planning &amp; Advisory</div>
  <div class="service-text">Outsourced financial planning and analysis (FP&amp;A) services, including model development, strategy valuation and exit options analysis.</div>
</div>

<!-- who we serve band -->
<svg class="abs" style="left:0;top:1517px" width="1200" height="1085" viewBox="0 0 1200 1085">
  <rect x="0" y="5" width="1200" height="1075" fill="#e5ecec"/>
  <polygon points="0,5 580,103 0,200" fill="#4d6c8a"/>
  <polygon points="0,200 580,103 0,212" fill="#ffffff"/>
  <polygon points="0,1080 617,980 1200,880 1200,1085 0,1085" fill="#ffffff"/>
  <polygon points="1200,880 617,980 1200,1080" fill="#4d6c8a"/>
</svg>
<h2 class="abs serve-title">Who Do We Serve</h2>

<div class="abs tile" style="left:75px;top:1834px;background:linear-gradient(135deg,#c7b7a8,#5d79a6 55%,#b3b8d6)" role="img" aria-label="Hand touching a glowing digital interface">
  <div class="tile-band">Technology</div></div>
<div class="abs tile" style="left:435px;top:1834px;background:linear-gradient(180deg,#c9cbce,#f1f2f2 50%,#9ea4a6)" role="img" aria-label="Bright factory floor with assembly lines">
  <div class="tile-band">Manufacturing</div></div>
<div class="abs tile" style="left:795px;top:1834px;background:linear-gradient(135deg,#8b8e90,#c9b59a 50%,#354a6b)" role="img" aria-label="Warehouse staff checking boxes on shelves">
  <div class="tile-band">Wholesale / Distribution</div></div>
<div class="abs tile" style="left:75px;top:2120px;background:linear-gradient(180deg,#b9c3c7,#2e3440 60%,#c6cbce)" role="img" aria-label="Group of business professionals standing together">
  <div class="tile-band">Business &amp; Professional</div></div>
<div class="abs tile" style="left:435px;top:2120px;background:linear-gradient(135deg,#6b5442,#a9876a 50%,#3f4147)" role="img" aria-label="Shop owner reviewing stock on a tablet">
  <div class="tile-band">Retail</div></div>
<div class="abs tile" style="left:795px;top:2120px;background:linear-gradient(180deg,#9fa7a4,#dedcd6 50%,#3d8a4f)" role="img" aria-label="Shopper with a green cart in a grocery aisle">
  <div class="tile-band">Consumer Products</div></div>

<!-- contact -->
<svg class="abs" style="left:0;top:2648px" width="620" height="490" viewBox="0 0 620 490">
  <defs>
    <linearGradient id="deskFill" x1="0" y1="0" x2="1" y2="1">
      <stop offset="0" stop-color="#2a3138"/>
      <stop offset="1" stop-color="#14161b"/>
    </linearGradient>
  </defs>
  <polygon role="img" aria-label="Dark photo of a man working at a laptop" points="0,0 465,0 614,490 0,490" fill="url(#deskFill)"/>
</svg>
<h2 class="abs section-heading" style="left:75px;top:2781px">Contact Us</h2>
<p class="abs section-copy" style="left:75px;top:2840px">Sed ut perspiciatis unde omnis iste natus error sit voluptatem accusantium doloremque laudantium, totam rem aperiam, eaque ipsa quae ab illo&nbsp; inventore veritatis et quasi architecto beatae vitae dicta sunt explicabo.</p>

<div class="abs form-card"></div>
<div class="abs field" style="left:456px;top:2780px;width:309px;height:40px">Full Name</div>
<div class="abs field" style="left:456px;top:2832px;width:309px;height:40px">Email Address</div>
<div class="abs field" style="left:456px;top:2886px;width:309px;height:40px">Phone No</div>
<div class="abs msg" style="left:794px;top:2780px;width:304px;height:149px">Message</div>
<div class="abs captcha" style="left:459px;top:2944px;width:305px;height:62px">
  <div class="abs" style="left:12px;top:19px;width:24px;height:24px;border:2px solid #c1c1c1;border-radius:2px;background:#fff"></div>
  <div class="abs" style="left:46px;top:23px;font-size:12px;color:#222">I'm not a robot</div>
  <div class="abs" style="left:257px;top:8px;width:22px;height:22px;background:#9aa8b8"></div>
  <div class="abs" style="left:236px;top:34px;font-size:7.5px;color:#666;width:62px;text-align:center;line-height:11px">HumanCheck<br>Privacy - Terms</div>
</div>
<div class="abs btn" style="left:795px;top:2955px;width:302px;height:41px;background:var(--blue);font-size:14px">Send »</div>

<!-- footer -->
<svg class="abs" style="left:0;top:3176px" width="1200" height="463" viewBox="0 0 1200 463">
  <rect x="0" y="5" width="1200" height="458" fill="#e5ecec"/>
  <polygon points="0,5 580,103 0,203" fill="#4d6c8a"/>
  <polygon points="0,203 580,103 0,215" fill="#ffffff"/>
</svg>
<div class="abs brand" style="top:3488px">
  <div class="brand-mark"></div>
  <div class="brand-name">MARLOWFEN<small>PRICING COUNSEL LLC</small></div>
</div>

<div class="abs foot-head" style="left:441px;top:3421px">Quick Links</div>
<div class="abs foot-rule" style="left:441px;top:3452px"></div>
<div class="abs foot-links" style="left:441px;top:3455px">Home<br>Services<br>Who Do We Serve<br>Industries<br>Contact Us</div>

<div class="abs foot-head" style="left:697px;top:3421px">References</div>
<div class="abs foot-rule" style="left:697px;top:3452px"></div>
<div class="abs foot-links" style="left:697px;top:3455px">Terms of Use<br>Privacy Policy</div>

<div class="abs foot-head" style="left:940px;top:3421px">Contact Info</div>
<div class="abs foot-rule" style="left:940px;top:3452px"></div>
<div class="abs foot-info" style="left:940px;top:3458px">
  <b>Marlowfen Pricing Counsel LLC</b><br>418 W Alder Ridge Rd Ste 12,<br>Kestrel Falls, ID 83702
</div>
<svg class="abs" style="left:940px;top:3531px" width="12" height="12" viewBox="0 0 12 12"><path d="M2 1h3l1 3-2 1a7 7 0 0 0 3 3l1-2 3 1v3c-6 1-10-3-9-9z" fill="#4d6c8a"/></svg>
<div class="abs foot-info" style="left:967px;top:3526px">+1 208 555 0142</div>
<svg class="abs" style="left:940px;top:3558px" width="12" height="10" viewBox="0 0 12 10"><rect x="0" y="0" width="12" height="10" fill="#4d6c8a"/><path d="M0 0l6 5 6-5" fill="none" stroke="#e5ecec" stroke-width="1.2"/></svg>
<div class="abs foot-info" style="left:967px;top:3552px">hello@marlowfencounsel.com</div>

<div class="abs bottom-bar">
  <div class="abs copyright">Copyright © 2022 Marlowfen Pricing Counsel LLC. All rights reserved</div>
  <div class="abs social" style="left:994px"></div>
  <div class="abs social" style="left:1020px"></div>
  <div class="abs social" style="left:1047px"></div>
  <div class="abs social" style="left:1074px"></div>
  <div class="abs social" style="left:1105px"></div>
</div>

</body>
</html>
```